Managed Service Provider need new business cards

We are a small Maanged Service Provider of IT Services and need a new fresh design for our business cards. We want something impossible, fun and professional :)
Our services has a large range, but we are always fun and make sure our customers both get their issue sorted and also feel like they are "catching up with an old friend".
All our cards in the past has always been all black, with red and we need something fresher.
The back of card, we would like just a small list of what we do i think, but if someone has a better idea, please do something cool with the back of the card:
Managed IT Services
Productivity Solutions
Data Backup and Recovery
IT System Maintenance
Managed IT Security
More details can be found on our website qvtechworks.com.au
Industry/Entity Type
It Company
Contact Information for Business Card
Name: Simon Trelawny
Title: Director
Phone: 03 6158 4932
Mobile: 0417 582 139
Email: simon@qvtechworks.com.au
Web: www.qvtechworks.com.au
Look and feel
Each slider illustrates characteristics of the customer's brand and the style your logo design should communicate.

```html
<!DOCTYPE html>
<html lang="en">
<head>
<meta charset="utf-8">
<title>QV TechWorks — Business Card</title>
<link rel="stylesheet" href="https://fonts.googleapis.com/css2?family=Open+Sans:wght@300;400;600;700&display=swap">
<style>
  :root {
    --brand-red: #e52027;
    --card-white: #f6f6f6;
    --ink: #2a2a2a;
    --backdrop: #d9d6d2;
  }
  * { box-sizing: border-box; margin: 0; padding: 0; }
  html, body {
    width: 1200px;
    height: 750px;
    overflow: hidden;
    background: var(--backdrop);
    font-family: "Open Sans", Arial, sans-serif;
  }
  .canvas {
    width: 1200px;
    height: 750px;
    display: flex;
    align-items: center;
    justify-content: center;
    gap: 60px;
  }
  .card {
    position: relative;
    width: 520px;
    height: 300px;
    overflow: hidden;
    box-shadow: 0 8px 20px rgba(0,0,0,0.18);
  }
  .card-front { background: var(--card-white); }
  .card-back { background: var(--brand-red); }
  .card-shape {
    position: absolute;
    inset: 0;
    width: 100%;
    height: 100%;
  }
  .contact-block {
    position: absolute;
    left: 34px;
    top: 30px;
  }
  .person-name {
    color: var(--brand-red);
    font-weight: 700;
    font-size: 21px;
    line-height: 1.1;
  }
  .person-title {
    color: var(--ink);
    font-size: 15px;
    font-weight: 400;
    margin-bottom: 14px;
  }
  .contact-list {
    list-style: none;
    font-size: 14px;
    line-height: 1.35;
    color: var(--ink);
  }
  .contact-label {
    color: var(--brand-red);
    display: inline-block;
    width: 22px;
  }
  .brand-name {
    position: absolute;
    font-weight: 700;
    font-size: 27px;
    letter-spacing: -0.3px;
    display: flex;
    align-items: center;
    gap: 8px;
  }
  .brand-name-front {
    left: 170px;
    bottom: 48px;
    color: var(--brand-red);
  }
  .brand-name-back {
    left: 236px;
    bottom: 40px;
    color: var(--card-white);
  }
  .brand-dot {
    width: 12px;
    height: 12px;
    border-radius: 50%;
    background: currentColor;
  }
  .service-list {
    position: absolute;
    left: 34px;
    top: 30px;
    list-style: none;
    color: var(--card-white);
    font-weight: 300;
    font-size: 16px;
    line-height: 1.6;
  }
</style>
</head>
<body>
  <main class="canvas">
    <section class="card card-front" aria-label="Business card front">
      <svg class="card-shape" viewBox="0 0 520 300" preserveAspectRatio="none" aria-hidden="true">
        <path d="M465 0 C425 90 400 225 300 300 L520 300 L520 0 Z" fill="var(--brand-red)"/>
      </svg>
      <div class="contact-block">
        <h1 class="person-name">Simon Trelawny</h1>
        <p class="person-title">Director</p>
        <ul class="contact-list">
          <li><span class="contact-label">P :</span>03 6158 4932</li>
          <li><span class="contact-label">M:</span>0417 582 139</li>
          <li><span class="contact-label">E :</span>simon@qvtechworks.com.au</li>
          <li><span class="contact-label">W:</span>www.qvtechworks.com.au</li>
        </ul>
      </div>
      <div class="brand-name brand-name-front">QV TechWorks</div>
    </section>

    <section class="card card-back" aria-label="Business card back">
      <svg class="card-shape" viewBox="0 0 520 300" preserveAspectRatio="none" aria-hidden="true">
        <path d="M475 0 C525 100 480 255 385 300 L520 300 L520 0 Z" fill="var(--card-white)"/>
      </svg>
      <ul class="service-list">
        <li>Managed IT Services</li>
        <li>Productivity Solutions</li>
        <li>Data Backup and Recovery</li>
        <li>IT System Maintenance</li>
        <li>Managed IT Security</li>
      </ul>
      <div class="brand-name brand-name-back">QV TechWorks</div>
    </section>
  </main>
</body>
</html>
```